Membership Card Design

I need a basic membership card...it will entitle the customer to free entry to forthcoming promotions.
The business is called ORBIT ARCADIA and is a amusement arcade located in N Ireland.
I require .....
ORBIT ARCADIA MEMBER...across top of card in logo format.
Next line....this card entitles the holder free entry to forthcoming ORBIT PROMOTIONS....
Then next line....customer name( space to write their name )
Next line.....customer mobile number ( space to write number )
On rear of card....logo/picture & ORBIT ARCADIA MEMBER written on back.

ORBIT ARCADIA
MEMBERSHIP CARD

```html
<!DOCTYPE html>
<html lang="en">
<head>
<meta charset="utf-8">
<title>Orbit Arcadia Membership Card</title>
<link rel="stylesheet" href="https://fonts.googleapis.com/css2?family=Oswald:wght@500;600&family=Bebas+Neue&display=swap">
<style>
  :root {
    --ink: #000000;
    --panel-glow: #1c1c1c;
    --silver-light: #f2f2f2;
    --silver-mid: #b9b9b9;
    --silver-dark: #6e6e6e;
    --bar-white: #ffffff;
  }
  html, body {
    margin: 0;
    padding: 0;
    width: 1200px;
    height: 791px;
    overflow: hidden;
    background: var(--ink);
  }
  .card {
    position: relative;
    width: 1200px;
    height: 791px;
    overflow: hidden;
    background:
      radial-gradient(ellipse 520px 300px at 580px 220px, var(--panel-glow) 0%, var(--ink) 70%),
      var(--ink);
    font-family: "Oswald", sans-serif;
  }
  .brand {
    position: absolute;
    left: 0;
    width: 1200px;
    top: 140px;
    text-align: center;
    margin: 0;
    font-family: "Oswald", sans-serif;
    font-weight: 500;
    font-size: 92px;
    line-height: 1;
    letter-spacing: 4px;
    color: var(--silver-light);
  }
  .silver {
    background: linear-gradient(180deg, var(--silver-light) 0%, var(--silver-light) 40%, var(--silver-dark) 100%);
    -webkit-background-clip: text;
    background-clip: text;
    color: transparent;
  }
  .entitlement {
    position: absolute;
    left: 0;
    width: 1156px;
    top: 372px;
    margin: 0;
    text-align: center;
    font-family: "Bebas Neue", sans-serif;
    font-size: 40px;
    line-height: 35px;
    letter-spacing: 0.5px;
  }
  .field-label {
    position: absolute;
    left: 0;
    width: 1160px;
    margin: 0;
    text-align: center;
    font-family: "Oswald", sans-serif;
    font-weight: 600;
    font-size: 52px;
    line-height: 1;
    letter-spacing: 0.5px;
    transform: scaleX(0.92);
  }
  .field-label.name { top: 452px; }
  .field-label.mobile { top: 584px; }
  .write-bar {
    position: absolute;
    background: linear-gradient(90deg,
      rgba(255,255,255,0) 0%,
      rgba(255,255,255,0.85) 12%,
      var(--bar-white) 30%,
      var(--bar-white) 70%,
      rgba(255,255,255,0.85) 88%,
      rgba(255,255,255,0) 100%);
    box-shadow: 0 0 18px rgba(255,255,255,0.25);
  }
  .write-bar::after {
    content: "";
    position: absolute;
    inset: 0;
    background: linear-gradient(180deg, rgba(0,0,0,0.25) 0%, rgba(0,0,0,0) 30%, rgba(0,0,0,0) 70%, rgba(0,0,0,0.3) 100%);
  }
  .write-bar.name { left: 277px; top: 516px; width: 612px; height: 62px; }
  .write-bar.mobile { left: 196px; top: 644px; width: 763px; height: 66px; }
</style>
</head>
<body>
  <main class="card">
    <h1 class="brand">ORBIT ARCADIA</h1>
    <p class="entitlement silver">This card entitles the holder free<br>entry to forthcoming ORBIT PROMOTIONS</p>
    <h2 class="field-label name silver">CUSTOMER NAME</h2>
    <div class="write-bar name" aria-label="Space to write customer name"></div>
    <h2 class="field-label mobile silver">CUSTOMER MOBILE NUMBER</h2>
    <div class="write-bar mobile" aria-label="Space to write customer mobile number"></div>
  </main>
</body>
</html>
```